Letterhead and Business Card for our company

We need a letterhead to our company with Business Cards.. This will be printed. The letter head is the official use for the company.

Note: Put in consideration that 2 languages will be used, you will design the English and we will add the Arabic.

Company name: Brisk Harbor
City: Jeddah
District: Alrehab
Center: Palmgate Plaza
Country: Saudi Arabia
POBox: 3872 Jeddah 23619

Industry/Entity Type

Startup

Font styles to use
Sans Serif

Requirements
Must have
• Capital: 100,000
• CR: 4817293058

```html
<!DOCTYPE html>
<html lang="en">
<head>
<meta charset="utf-8">
<title>Brisk Harbor — Letterhead and Business Cards</title>
<link href="https://fonts.googleapis.com/css2?family=Roboto:wght@400;500;700&display=swap" rel="stylesheet">
<style>
  :root {
    --canvas: #ffffff;
    --paper: #fafafa;
    --card: #34373c;
    --ink: #2f3237;
    --white: #ffffff;
    --blue: #3d9ac6;
    --green: #6f9e1a;
    --red: #d9152a;
    --plum: #8d1659;
    --violet: #5a4d9a;
    --soft-grey: #c9ccd1;
  }
  * { margin: 0; padding: 0; box-sizing: border-box; }
  html, body {
    width: 1200px; height: 1200px; overflow: hidden;
    background: var(--canvas);
    font-family: "Roboto", Arial, sans-serif;
  }
  .stage { position: relative; width: 1200px; height: 1200px; }

  /* Letterhead */
  .letterhead {
    position: absolute; left: 434px; top: 130px;
    width: 592px; height: 836px;
    background: var(--paper);
  }
  .letterhead-brand {
    position: absolute; left: 39px; top: 62px;
    display: flex; align-items: center; gap: 10px;
  }
  .brand-dot { width: 34px; height: 34px; border-radius: 50%; background: var(--blue); }
  .brand-name {
    font-weight: 500; color: var(--ink);
    font-size: 22px; letter-spacing: 0.5px; white-space: nowrap;
  }
  .letterhead-footer {
    position: absolute; left: 39px; right: 81px; top: 777px;
    display: flex; justify-content: space-between;
    font-size: 10px; line-height: 13px; color: var(--ink);
  }
  .stripe {
    position: absolute; left: 0; right: 0; bottom: 0;
    display: flex; height: 9px;
  }
  .stripe span { flex: 1; }
  .c-blue { background: var(--blue); }
  .c-green { background: var(--green); }
  .c-red { background: var(--red); }
  .c-plum { background: var(--plum); }
  .c-violet { background: var(--violet); }

  /* Business cards */
  .card {
    position: absolute; left: 147px; width: 256px; height: 155px;
    background: var(--card); overflow: hidden;
  }
  .card-front { top: 384px; }
  .card-back { top: 558px; height: 154px; }
  .card-front .card-brand {
    position: absolute; left: 0; right: 0; top: 62px;
    display: flex; justify-content: center; align-items: center; gap: 8px;
  }
  .card-front .brand-dot { width: 24px; height: 24px; }
  .card-front .brand-name { color: var(--white); font-size: 18px; }
  .card-front .stripe { height: 4px; }

  .card-symbol {
    position: absolute; left: 33px; top: 40px;
    width: 58px; height: 58px; border-radius: 50%;
    background: var(--blue);
  }
  .card-details { position: absolute; left: 132px; top: 31px; color: var(--white); }
  .card-name { font-weight: 500; font-size: 10.5px; line-height: 12px; }
  .card-title { font-size: 5.5px; line-height: 7px; margin-bottom: 9px; }
  .contact-list { list-style: none; font-size: 6.3px; line-height: 9.5px; }
  .contact-list li { display: flex; align-items: center; gap: 5px; }
  .contact-list svg { width: 6px; height: 6px; fill: var(--white); flex: none; }
  .card-address { font-size: 6.3px; line-height: 9.5px; margin-top: 2px; }
  .card-base { position: absolute; left: 0; bottom: 0; width: 256px; height: 20px; }
  .card-web {
    position: absolute; left: 132px; bottom: 6px;
    font-size: 6.3px; color: var(--white);
  }
</style>
</head>
<body>
<main class="stage">

  <section class="letterhead" aria-label="Letterhead">
    <div class="letterhead-brand">
      <span class="brand-dot"></span>
      <span class="brand-name">Brisk Harbor</span>
    </div>
    <footer class="letterhead-footer">
      <address style="font-style:normal">3872 Jeddah 23619<br>Palmgate Plaza Jeddah Saudi Arabia</address>
      <p>Capital: 100,000<br>CR: 4817293058</p>
    </footer>
    <div class="stripe">
      <span class="c-blue"></span><span class="c-green"></span><span class="c-red"></span><span class="c-plum"></span><span class="c-violet"></span>
    </div>
  </section>

  <section class="card card-front" aria-label="Business card front">
    <div class="card-brand">
      <span class="brand-dot"></span>
      <span class="brand-name">Brisk Harbor</span>
    </div>
    <div class="stripe">
      <span class="c-blue"></span><span class="c-green"></span><span class="c-red"></span><span class="c-plum"></span><span class="c-violet"></span>
    </div>
  </section>

  <section class="card card-back" aria-label="Business card back">
    <div class="card-symbol" role="img" aria-label="Company emblem area"></div>
    <div class="card-details">
      <p class="card-name">Brisk Harbor</p>
      <p class="card-title">Managing Director</p>
      <ul class="contact-list">
        <li><svg viewBox="0 0 10 10"><rect x="2.5" y="0" width="5" height="10" rx="1"/></svg>+111 222 3333</li>
        <li><svg viewBox="0 0 10 10"><path d="M0 4 Q5 0 10 4 L8 5 L7 3.5 L3 3.5 L2 5 Z M2 6 H8 V10 H2 Z"/></svg>+444 555 6666</li>
        <li><svg viewBox="0 0 10 10"><path d="M0 2 H10 V8 H0 Z M0.8 2.6 L5 5.6 L9.2 2.6" stroke="#34373c" stroke-width="0.8"/></svg>yourname@yourwebsite.com</li>
      </ul>
      <p class="card-address">3872 Jeddah 23619<br>Palmgate Plaza Jeddah Saudi Arabia</p>
    </div>
    <svg class="card-base" viewBox="0 0 256 20" preserveAspectRatio="none" aria-hidden="true">
      <rect x="0" y="11" width="30" height="9" fill="#8d1659"/>
      <rect x="30" y="11" width="31" height="9" fill="#d9152a"/>
      <rect x="61" y="11" width="30" height="9" fill="#6f9e1a"/>
      <rect x="91" y="11" width="18" height="9" fill="#5a4d9a"/>
      <polygon points="103,20 118,0 256,0 256,20" fill="#3d9ac6"/>
    </svg>
    <p class="card-web">www.yourwebsite.com</p>
  </section>

</main>
</body>
</html>
```